A website design for a consultation firm

We are located in Istanbul, Turkey and offers our consultation services to customers interested in investing in Realestate, Education and Investment particularly this coming from Arab world and English speaking countries.

The site should carry our message of deep knowledge about the Turkish markets in the mentioned sectors of interest, sincerity and keenness.

The final deliverable of the winning design should include:
- The source files of the final designs. e.g. AI, PSD ..etc
- The redline markup for the design using a Specctr or any other similar tool.

Target Market(s)

English and Arabic speaking countries with a Turkish theme since we are a Turkish company

Industry/Entity Type

Consulting

Number of Pages Required

2 page

Font styles to use
Sans Serif

Requirements
Must have
• The site should serve the following main sections:
• - Why QVD?
• - Reports & studies
• - Sectors
• - Our team
• - Contact
• We need a design that could be converted into a WordPress theme.
• The design should be in English but should accommodate other languages including RTL.
• You can use the color theme you like as long as it does't dissolve the logo.
• The site should link into our accounts on the following networks:
• - Twitter
• - Facebook
• - LinkedIn
• The design should be responsive and nicely rendered on Desktop, Tablets and Smart phones.
Nice to have
• The site would be nice to balance between being informative and

```html
<!DOCTYPE html>
<html lang="en">
<head>
<meta charset="utf-8">
<title>QVD Consulting</title>
<link rel="stylesheet" href="https://fonts.googleapis.com/css2?family=Roboto:wght@300;400;500;700&family=Lato:wght@700;900&display=swap">
<style>
:root{
  --navy:#1b3867;
  --red:#c8070e;
  --grey-bg:#efefef;
  --text-muted:#9a9a9a;
  --text-dark:#444;
  --line:#8a8a8a;
  --white:#fff;
}
*{box-sizing:border-box;margin:0;padding:0}
html,body{width:1200px;height:2773px;overflow:hidden}
body{position:relative;font-family:'Roboto',Arial,sans-serif;background:var(--white);color:var(--text-dark)}
.abs{position:absolute}

/* header */
.site-header{position:absolute;left:0;top:0;width:1200px;height:126px;background:var(--white);box-shadow:0 3px 6px rgba(0,0,0,.35);z-index:3}
.brand{left:78px;top:22px;display:flex;align-items:center;gap:12px}
.brand-dot{width:26px;height:26px;border-radius:50%;background:var(--red)}
.brand-name{font-size:40px;font-weight:700;color:var(--red);line-height:1}
.brand-sub{left:116px;top:72px;font-size:22px;font-weight:400;color:var(--red)}
.top-contact{top:18px;height:30px;display:flex;align-items:center;gap:12px;font-size:14px;color:#555}
.top-contact.email{left:692px}
.top-contact.phone{left:962px;padding-left:0}
.top-sep{left:948px;top:0;width:1px;height:60px;background:#e2e2e2}
.top-rule{left:948px;top:60px;width:176px;height:1px;background:#e2e2e2}
.main-nav{left:388px;top:82px;display:flex;gap:0;font-size:16px;color:#666;text-transform:uppercase}
.main-nav a{display:block;padding:0 18px;height:44px;line-height:24px;color:inherit;text-decoration:none;position:relative}
.main-nav a.active{color:var(--red)}
.main-nav a.active::after{content:"";position:absolute;left:0;right:0;bottom:0;height:4px;background:var(--red)}

/* hero */
.hero{left:0;top:126px;width:1200px;height:549px;background:linear-gradient(180deg,#1f5fa8 0%,#1f80c8 55%,#3fc0ee 100%);overflow:hidden}
.hero-visual{left:360px;top:0;width:840px;height:549px;background:linear-gradient(160deg,#2a64a8 0%,#a9b4bf 45%,#e3e6e8 70%,#5a7c5a 100%);clip-path:polygon(18% 0,100% 0,100% 100%,0 100%,6% 60%)}
.hero-title{left:78px;top:205px;font-family:'Lato',Arial,sans-serif;font-weight:900;font-size:52px;line-height:60px;text-transform:uppercase;z-index:2}
.hero-title .l1{color:var(--navy);display:block}
.hero-title .l2{color:var(--white);display:block;font-weight:700;font-size:48px}
.btn{display:flex;align-items:center;justify-content:center;background:var(--navy);color:var(--white);font-size:20px;text-transform:uppercase}
.hero .btn{left:78px;top:338px;width:250px;height:62px}

/* sector cards */
.sector{top:649px;width:312px;height:272px;color:var(--white);text-align:center;box-shadow:0 18px 14px -12px rgba(0,0,0,.35);z-index:2}
.sector.navy{background:var(--navy)}
.sector.red{background:var(--red)}
.sector-icon{position:absolute;left:93px;top:-63px;width:126px;height:126px;border-radius:50%;background:var(--white);border:4px solid var(--navy);display:flex;align-items:center;justify-content:center}
.sector.red .sector-icon{border-color:var(--red)}
.sector h3{position:absolute;left:0;right:0;top:87px;font-size:18px;font-weight:400;letter-spacing:.5px}
.sector p{position:absolute;left:22px;right:22px;top:121px;font-size:14px;line-height:27px}
.sector .chev{position:absolute;left:146px;top:215px}

/* sections */
.section-title{left:0;width:1200px;text-align:center;font-size:40px;font-weight:400;text-transform:uppercase;color:var(--navy)}
.section-title .accent{color:var(--red)}
.lead{left:140px;width:920px;text-align:center;font-size:15px;line-height:27px;color:var(--text-muted)}
.team-band{left:0;top:1285px;width:1200px;height:521px;background:var(--grey-bg)}
.member{top:1424px;width:251px;height:318px;background:#f7f7f7;border-bottom:4px solid var(--red);box-shadow:0 2px 5px rgba(0,0,0,.25)}
.member-photo{width:100%;height:229px;background:linear-gradient(180deg,#d8d2c8 0%,#b9aa98 100%)}
.member h4{position:absolute;left:12px;top:250px;font-size:18px;font-weight:400;color:var(--red);text-transform:uppercase}
.member p{position:absolute;left:12px;top:283px;font-size:16px;color:#8a8a8a}

.callback{left:0;top:1806px;width:1200px;height:156px;background:var(--red)}
.callback h2{position:absolute;left:80px;top:56px;font-size:40px;font-weight:400;color:var(--white);text-transform:uppercase;line-height:44px}
.callback .btn-white{position:absolute;left:893px;top:50px;width:229px;height:63px;background:var(--white);color:var(--red);display:flex;align-items:center;justify-content:center;font-size:20px;text-transform:uppercase}

/* footer */
.footer{left:0;top:2308px;width:1200px;height:403px;background:var(--grey-bg)}
.footer-divider{left:600px;top:0;width:2px;height:403px;background:#bcbcbc}
.footer h5{position:absolute;font-size:20px;font-weight:400;color:var(--red);text-transform:uppercase}
.field{position:absolute;left:78px;width:416px;border:1px solid var(--line);background:transparent;font-size:14px;color:#999;padding:14px 14px}
.send{left:78px;top:286px;width:166px;height:63px}
.touch-item{position:absolute;left:654px;display:flex;gap:18px;font-size:15px;color:#555;line-height:24px;width:420px}
.touch-item svg{flex:none;margin-top:4px}
.newsletter{position:absolute;left:640px;top:297px;width:473px;height:52px;border:1px solid var(--line);font-size:14px;color:#999;padding:16px 20px}
.newsletter svg{position:absolute;right:16px;top:13px}

.bottom-bar{left:0;top:2711px;width:1200px;height:62px;background:var(--white)}
.copyright{left:78px;top:20px;font-size:16px;color:#222}
.copyright b{color:var(--red);font-weight:400}
.social{top:11px;width:40px;height:40px;border-radius:50%;border:2px solid #777}
.social.solid{background:var(--red);border-color:var(--red)}
</style>
</head>
<body>

<header class="site-header">
  <div class="abs brand"><span class="brand-dot"></span><span class="brand-name">QVD</span></div>
  <div class="abs brand-sub">consulting</div>
  <div class="abs top-contact email">
    <svg width="18" height="13" viewBox="0 0 18 13"><rect width="18" height="13" fill="#c8070e"/><path d="M0 0 9 7 18 0" fill="none" stroke="#fff" stroke-width="1.5"/></svg>
    infotech@QVD Consulting.com
  </div>
  <div class="abs top-sep"></div>
  <div class="abs top-rule"></div>
  <div class="abs top-contact phone">
    <svg width="18" height="18" viewBox="0 0 24 24"><path d="M6.6 10.8a15 15 0 0 0 6.6 6.6l2.2-2.2c.3-.3.7-.4 1-.2 1.1.4 2.3.6 3.6.6.6 0 1 .4 1 1V20c0 .6-.4 1-1 1A17 17 0 0 1 3 4c0-.6.4-1 1-1h3.5c.6 0 1 .4 1 1 0 1.3.2 2.5.6 3.6.1.3 0 .7-.2 1z" fill="#c8070e"/></svg>
    +(90) 0212 555 0148
  </div>
  <nav class="abs main-nav">
    <a class="active">Home</a><a>Why QVD ?</a><a>Reports &amp; Studies</a><a>Sectors</a><a>Our Team</a><a>Contact</a>
  </nav>
</header>

<section class="abs hero">
  <div class="abs hero-visual" role="img" aria-label="Aerial view of white high-rise residential towers"></div>
  <h1 class="abs hero-title"><span class="l1">Unlock the Turkish</span><span class="l2">Market for Investors</span></h1>
  <div class="abs btn">Contact Now Us</div>
</section>

<article class="abs sector navy" style="left:98px">
  <div class="sector-icon">
    <svg width="70" height="60" viewBox="0 0 70 60"><path d="M4 30 30 6 56 30" fill="none" stroke="#c8070e" stroke-width="6"/><path d="M12 28v26h24" fill="none" stroke="#c8070e" stroke-width="6"/><circle cx="48" cy="42" r="15" fill="none" stroke="#c8070e" stroke-width="4"/><path d="M52 35c-2-2-9-2-9 2s9 2 9 7-8 5-10 2M47 31v22" fill="none" stroke="#c8070e" stroke-width="3"/></svg>
  </div>
  <h3>REALESTATE</h3>
  <p>Lorem Ipsum is simply dummy text of the printing and typesetting industry. Lorem Ipsum has been the.</p>
  <svg class="chev" width="20" height="18" viewBox="0 0 20 18"><path d="M3 2l7 6 7-6M3 9l7 6 7-6" fill="none" stroke="#fff" stroke-width="2"/></svg>
</article>
<article class="abs sector red" style="left:444px">
  <div class="sector-icon">
    <svg width="76" height="56" viewBox="0 0 76 56"><path d="M38 4 74 18 38 32 2 18z" fill="#c8070e"/><path d="M18 26v16c10 8 30 8 40 0V26L38 34z" fill="#c8070e"/><path d="M68 20v20" stroke="#c8070e" stroke-width="3"/></svg>
  </div>
  <h3>EDUCATION</h3>
  <p>Lorem Ipsum is simply dummy text of the printing and typesetting industry. Lorem Ipsum has been the.</p>
  <svg class="chev" width="20" height="18" viewBox="0 0 20 18"><path d="M3 2l7 6 7-6M3 9l7 6 7-6" fill="none" stroke="#fff" stroke-width="2"/></svg>
</article>
<article class="abs sector navy" style="left:789px">
  <div class="sector-icon">
    <svg width="70" height="60" viewBox="0 0 70 60"><rect x="6" y="42" width="9" height="16" fill="#c8070e"/><rect x="20" y="34" width="9" height="24" fill="#c8070e"/><rect x="34" y="38" width="9" height="20" fill="#c8070e"/><rect x="48" y="26" width="9" height="32" fill="#c8070e"/><path d="M6 34 24 18 38 28 60 8" fill="none" stroke="#c8070e" stroke-width="4"/><path d="M50 6h12v12z" fill="#c8070e"/></svg>
  </div>
  <h3>INVESTMENT</h3>
  <p>Lorem Ipsum is simply dummy text of the printing and typesetting industry. Lorem Ipsum has been the.</p>
  <svg class="chev" width="20" height="18" viewBox="0 0 20 18"><path d="M3 2l7 6 7-6M3 9l7 6 7-6" fill="none" stroke="#fff" stroke-width="2"/></svg>
</article>

<h2 class="abs section-title" style="top:980px"><span class="accent">Welcome to</span> QVD Consulting</h2>
<p class="abs lead" style="top:1038px">Lorem Ipsum is simply dummy text of the printing and typesetting industry. Lorem Ipsum has been the industry's standard dummy text ever since the 1500s, when an unknown printer took a galley of type and scrambled it to make a type specimen book. It has survived not only five centuries, but also the leap into electronic typesetting, remaining essentially unchanged. It was popularised in the 1960s with the release of Letraset sheets containing Lorem Ipsum passages</p>
<div class="abs btn" style="left:512px;top:1159px;width:176px;height:63px">Know More</div>

<section class="abs team-band"></section>
<h2 class="abs section-title" style="top:1344px"><span class="accent">Our</span> Team</h2>
<div class="abs member" style="left:78px"><div class="member-photo" role="img" aria-label="Portrait photo of a team member"></div><h4>Member Name</h4><p>Something.com</p></div>
<div class="abs member" style="left:344px"><div class="member-photo" role="img" aria-label="Portrait photo of a team member"></div><h4>Member Name</h4><p>Something.com</p></div>
<div class="abs member" style="left:608px"><div class="member-photo" role="img" aria-label="Portrait photo of a team member"></div><h4>Member Name</h4><p>Something.com</p></div>
<div class="abs member" style="left:873px"><div class="member-photo" role="img" aria-label="Portrait photo of a team member"></div><h4>Member Name</h4><p>Something.com</p></div>

<section class="abs callback">
  <h2>QVD Consulting Request Call Back</h2>
  <div class="btn-white">Call Us Know</div>
</section>

<h2 class="abs section-title" style="top:2023px"><span class="accent">Our</span> Reports &amp; Studies</h2>
<p class="abs lead" style="top:2084px">Lorem Ipsum is simply dummy text of the printing and typesetting industry. Lorem Ipsum has been the industry's standard dummy text ever since the 1500s, when an unknown printer took a galley of type and scrambled it to make a type specimen book. It has survived not only five centuries.</p>
<div class="abs btn" style="left:512px;top:2184px;width:176px;height:62px">Know More</div>

<footer class="abs footer">
  <div class="abs footer-divider"></div>
  <h5 style="left:80px;top:40px">Contact Us</h5>
  <div class="field" style="top:77px;height:47px">Name*</div>
  <div class="field" style="top:133px;height:47px">Email*</div>
  <div class="field" style="top:186px;height:91px">Message*</div>
  <div class="abs btn send">Send</div>

  <h5 style="left:654px;top:40px">Get In Touch</h5>
  <div class="touch-item" style="top:88px">
    <svg width="12" height="20" viewBox="0 0 12 20"><rect x="1" y="1" width="10" height="18" rx="2" fill="none" stroke="#c8070e" stroke-width="2"/><circle cx="6" cy="15" r="1.3" fill="#c8070e"/></svg>
    + (90) 212 555 0149
  </div>
  <div class="touch-item" style="top:132px">
    <svg width="14" height="20" viewBox="0 0 14 20"><path d="M7 0a7 7 0 0 0-7 7c0 5 7 13 7 13s7-8 7-13a7 7 0 0 0-7-7z" fill="#c8070e"/><circle cx="7" cy="7" r="2.5" fill="#fff"/></svg>
    <span>Lorem Ipsum is simply dummy text of the printing and typesetting&nbsp; simply dummy te..</span>
  </div>
  <div class="touch-item" style="top:188px">
    <svg width="18" height="13" viewBox="0 0 18 13"><rect width="18" height="13" fill="#c8070e"/><path d="M0 0 9 7 18 0" fill="none" stroke="#fff" stroke-width="1.5"/></svg>
    infotech@QVD Consulting.com
  </div>
  <h5 style="left:642px;top:256px">Newsletter</h5>
  <div class="newsletter">Enter Email id here
    <svg width="24" height="24" viewBox="0 0 24 24"><path d="M22 2 2 10l8 3 3 8z M22 2 10 13" fill="none" stroke="#c8070e" stroke-width="2" stroke-linejoin="round"/></svg>
  </div>
</footer>

<div class="abs bottom-bar">
  <p class="abs copyright">©<b>QVD Consulting</b> - 2016. All Rights Reserved.</p>
  <span class="abs social solid" style="left:978px"></span>
  <span class="abs social" style="left:1030px"></span>
  <span class="abs social" style="left:1082px"></span>
</div>

</body>
</html>
```